B2B EDM Banner Design- Specialist Tech Company

We need a new top-of-email banner for our EDM campaigns for Varnel Brix (www.varnelbrix-example.com
). This banner will sit at the top of every email and must immediately signal the brand, look modern and professional, and be visually aligned with the tech/IT audience.
Size of the banner: Around 728x90 - it must fit at the top of an email blast.
Purpose of the Banner
Establish a strong, recognizable brand identity across all Varnel Brix EDMs
visually consistent with existing banners created for other brands (see reference examples provided)
Communicate Varnel Brix’s value proposition at a glance
Brand Name
Varnel Brix
Tagline (must appear in the banner)
“11,322 whitepapers from 726 companies”
Design Requirements
Style & Tone
Modern, clean, and professional
Tech-centric look and feel
High-quality, sleek, and corporate
Eye-catching but not cluttered
Should feel premium and authoritative
Layout & Composition
Full-width banner for email header
Horizontal orientation similar to the Plomtar and Quindle Staff Archive examples
Include space for the brand name/logo prominently on the left or centered
Integrate the tagline in a readable, secondary position
Optional: a subtle background texture or tech-related abstract pattern (circuitry, network nodes, gradient, etc.)
No busy imagery—should feel clean and trustworthy
Color Palette
Use colors consistent with Varnel Brix branding from www.varnelbrix-example.com
Blues, greys, blacks, and tech-style gradients preferred
Should feel consistent with a B2B IT audience
Typography
Clean, sans-serif fonts (professional/tech-aligned)
Brand name should be bold and prominent
Tagline should be smaller, but still readable on desktop and mobile
Imagery (if used)
Abstract tech shapes, network visuals, geometric patterns, or gradient overlays
Avoid photography of people
Keep imagery subtle so text remains legible
Call-to-Action Button (optional)
None required in this banner (unlike the HR examples)
Banner should remain a pure brand header
Deliverables
Final banner in PNG and JPG formats
2–3 design variations (if possible) for A/B testing
Dimensions optimized for EDM: ~600–700px wide (standard email width), proportionate height

```html
<!DOCTYPE html>
<html lang="en">
<head>
<meta charset="utf-8">
<title>Varnel Brix – EDM Header Banner Variations</title>
<link rel="stylesheet" href="https://fonts.googleapis.com/css2?family=Montserrat:wght@400;500;600;700;800&display=swap">
<style>
  :root {
    --page-bg: #ffffff;
    --label-ink: #1b1b1b;
    --navy-flat: #1a1850;
    --navy-deep: #070c33;
    --navy-mid: #0f1a78;
    --royal: #1626a6;
    --cyan: #1aa3e0;
    --white: #ffffff;
  }
  * { box-sizing: border-box; margin: 0; padding: 0; }
  html, body {
    width: 1200px; height: 1200px; overflow: hidden;
    background: var(--page-bg);
    font-family: "Montserrat", Arial, sans-serif;
  }
  .sheet { position: relative; width: 1200px; height: 1200px; }

  .sheet-title {
    position: absolute; top: 204px; left: 0; width: 1200px;
    text-align: center; font-size: 11px; font-weight: 500; color: var(--label-ink);
  }
  .variation-label {
    position: absolute; left: 62px; font-size: 11px; font-weight: 500; color: var(--label-ink);
  }

  .banner {
    position: absolute; left: 62px; width: 1108px; height: 137px; overflow: hidden;
    color: var(--white);
  }
  .banner--flat { top: 293px; background: var(--navy-flat); }
  .banner--glow {
    background:
      radial-gradient(ellipse 60% 110% at 55% 0%, var(--royal) 0%, rgba(22,38,166,0) 70%),
      linear-gradient(20deg, var(--navy-deep) 0%, var(--navy-mid) 40%, #131f92 100%);
  }
  .banner--second { top: 512px; }
  .banner--third { top: 717px; }

  .brand-name {
    position: absolute; font-weight: 800; color: var(--white);
    letter-spacing: 0.5px; text-transform: uppercase; line-height: 1; white-space: nowrap;
  }
  .accent { color: var(--cyan); }

  .tagline { position: absolute; font-weight: 700; white-space: nowrap; line-height: 1.15; }

  .globe-visual { position: absolute; border-radius: 50%; }
  .globe-visual--wire {
    left: 63px; top: 1px; width: 135px; height: 135px;
    background: radial-gradient(circle, rgba(26,38,140,0.2) 40%, rgba(40,70,230,0.55) 68%, rgba(40,70,230,0) 72%);
  }
  .globe-visual--glass {
    left: 63px; top: 0; width: 130px; height: 137px;
    background: radial-gradient(circle at 55% 30%, rgba(90,140,255,0.65) 0%, rgba(30,60,190,0.45) 45%, rgba(10,20,80,0.2) 72%);
  }

  .binary-field { position: absolute; top: 0; height: 137px; }
  .binary-field--wide {
    left: 725px; width: 388px;
    background: radial-gradient(ellipse 50% 60% at 50% 50%, rgba(30,150,230,0.28) 0%, rgba(30,150,230,0) 80%);
  }
  .binary-field--edge {
    left: 1008px; width: 100px;
    background: linear-gradient(90deg, rgba(30,150,230,0) 0%, rgba(30,150,230,0.25) 100%);
  }

  .support-copy {
    position: absolute; left: 815px; top: 23px; width: 140px;
    text-align: center; font-size: 11.5px; font-weight: 600; line-height: 12.8px;
  }

  .brand-dot {
    position: absolute; left: 82px; top: 26px; width: 86px; height: 86px;
    border-radius: 50%; background: var(--cyan);
  }
  .contact-pill {
    position: absolute; left: 561px; top: 58px; width: 419px; height: 45px;
    border: 2px solid var(--cyan); border-radius: 23px;
    display: flex; align-items: center; justify-content: center;
    text-align: center; font-size: 11.8px; font-weight: 500; line-height: 14px;
  }
</style>
</head>
<body>
<main class="sheet">
  <p class="sheet-title">Banner size: 728 x 90 pixels</p>

  <p class="variation-label" style="top:267px;">1st variation</p>
  <section class="banner banner--flat" aria-label="Varnel Brix banner, variation 1">
    <div class="globe-visual globe-visual--wire" role="img" aria-label="Blue wireframe network globe"></div>
    <h1 class="brand-name" style="left:211px; top:44px; font-size:35px;">Varnel Brix</h1>
    <p class="tagline" style="left:555px; top:73px; font-size:18.5px;">
      <span class="accent">11,322</span> whitepapers from <span class="accent">726</span> companies
    </p>
  </section>

  <p class="variation-label" style="top:486px;">2nd variation</p>
  <section class="banner banner--glow banner--second" aria-label="Varnel Brix banner, variation 2">
    <div class="globe-visual globe-visual--glass" role="img" aria-label="Glowing hexagon-mesh globe"></div>
    <div class="binary-field binary-field--wide" role="img" aria-label="Flowing binary digit pattern"></div>
    <h1 class="brand-name" style="left:196px; top:38px; font-size:42px;">Varnel Brix</h1>
    <p class="tagline" style="left:604px; top:50px; font-size:16px; line-height:18.5px;">
      <span class="accent">11,322</span> whitepapers<br>from <span class="accent">726</span> companies
    </p>
    <p class="support-copy">Helping them<br>to assess,<br>analyse and review<br>their business<br>needs within<br>the fast paced<br>technology matrix.</p>
  </section>

  <p class="variation-label" style="top:692px;">3rd variation</p>
  <section class="banner banner--glow banner--third" aria-label="Varnel Brix banner, variation 3">
    <span class="brand-dot" aria-hidden="true"></span>
    <h1 class="brand-name" style="left:189px; top:38px; font-size:42px;">Varnel Brix</h1>
    <p class="tagline" style="left:570px; top:32px; width:400px; text-align:center; font-size:15px;">
      <span class="accent">11,322</span> whitepapers from <span class="accent">726</span> companies
    </p>
    <p class="contact-pill">Get in touch, and we can help you assess, analyze, and review<br>your business needs within the fast-paced technology matrix</p>
    <div class="binary-field binary-field--edge" role="img" aria-label="Binary digit pattern fading in"></div>
  </section>
</main>
</body>
</html>
```